Plumbing Company After Business Card

Business card for a plumbing business that offers a variety of plumbing services including maintenance, domestic and commercial plumbing. My main focus is to offer high quality professional service. A logo on the card would be ideal. Any other questions feel free to email. Cheers

Looking for something modern and upmarket with preferably a matte black background

Business name is Crestline Plumbing and Gas

Industry/Entity Type

Plumbing

Contact Information for Business Card

Crestline Plumbing and Gas
Marcus Thorvale
0472519306
14 Karrabee Drive, Kelbrook 3557
crestlineplumbing@mailbay.com.au
ABN 64 915 207 338

Font styles to use
Sans Serif

Colors
1b1b1b
ffffff
3377b5

Requirements
Must have
• Domestic
• Commercial
• Maintenance

```html
<!DOCTYPE html>
<html lang="en">
<head>
<meta charset="utf-8">
<title>Crestline Plumbing and Gas — Business Card</title>
<link href="https://fonts.googleapis.com/css2?family=Exo+2:wght@400;500;700;800&display=swap" rel="stylesheet">
<style>
  :root {
    --page: #ebe8e8;
    --card: #000000;
    --card-soft: #1b1b1b;
    --sheen: #2e2e2e;
    --white: #ffffff;
    --blue: #3377b5;
    --blue-bright: #1a86d0;
  }
  * { margin: 0; padding: 0; box-sizing: border-box; }
  html, body {
    width: 1200px; height: 1200px; overflow: hidden;
    background: var(--page);
    font-family: "Exo 2", sans-serif;
    color: var(--white);
  }
  .card {
    position: absolute;
    width: 660px; height: 410px;
    background: var(--card);
    overflow: hidden;
    box-shadow: 2px 3px 4px rgba(0,0,0,0.35);
  }
  .card--front { left: 100px; top: 140px; }
  .card--back {
    left: 440px; top: 610px;
    background: radial-gradient(ellipse 62% 62% at 52% 48%, var(--sheen) 0%, var(--card-soft) 45%, var(--card) 100%);
  }
  .front-sheen {
    position: absolute; inset: 0;
    background: radial-gradient(circle at 25% 62%, #333 0%, #1e1e1e 45%, #111 100%);
    clip-path: polygon(0 0, 58% 0, 26% 100%, 0 100%);
  }
  .brand {
    position: absolute;
    display: flex; align-items: center; gap: 12px;
    font-weight: 800; color: var(--blue-bright);
    text-transform: uppercase; line-height: 1.02;
  }
  .brand-dot { border-radius: 50%; background: var(--white); flex: none; }
  .card--front .brand { left: 40px; top: 78px; font-size: 34px; }
  .card--front .brand-dot { width: 36px; height: 36px; }
  .card--back .brand { left: 188px; top: 138px; font-size: 42px; }
  .card--back .brand-dot { width: 44px; height: 44px; }

  .person {
    position: absolute; right: 40px; top: 40px;
    text-align: right;
  }
  .person-name { font-size: 28px; font-weight: 800; letter-spacing: 0.5px; }
  .person-name .first { color: var(--blue-bright); }
  .contact-line {
    display: flex; align-items: center; justify-content: flex-end; gap: 8px;
    font-size: 21px; font-weight: 500; letter-spacing: 1px; line-height: 1.25;
  }
  .icon { width: 20px; height: 20px; flex: none; }
  .details {
    position: absolute; right: 40px; bottom: 34px;
    text-align: right;
  }
  .details .contact-line { font-size: 21px; letter-spacing: 0.5px; }
  .details .address { align-items: flex-start; }
  .details .address .icon { margin-top: 4px; }

  .services {
    position: absolute; left: 0; right: 0; bottom: 36px;
    height: 48px;
    display: flex; align-items: center; justify-content: space-around;
    background: linear-gradient(90deg, transparent, rgba(0,0,0,0.85) 10%, rgba(0,0,0,0.85) 90%, transparent);
    font-size: 21px; font-weight: 500; letter-spacing: 0.5px;
  }
  .service { display: flex; align-items: center; gap: 8px; }
  .service .tick { width: 18px; height: 18px; }
</style>
</head>
<body>

<section class="card card--front" aria-label="Business card front">
  <div class="front-sheen"></div>

  <div class="brand">
    <span class="brand-dot"></span>
    <span>Crestline<br>Plumbing<br>and Gas</span>
  </div>

  <div class="person">
    <p class="person-name"><span class="first">Marcus</span>Thorvale</p>
    <p class="contact-line">
      <svg class="icon" viewBox="0 0 24 24" fill="none" stroke="var(--blue-bright)" stroke-width="2">
        <circle cx="12" cy="12" r="10"/>
        <path d="M8.5 7.5c-.8.8-.6 3 1.6 5.4 2.3 2.4 4.6 2.8 5.5 2l1-1-2-1.8-1.1.9c-.8-.3-2.3-1.700-2.7-2.6l.9-1.1L9.8 7z" fill="var(--blue-bright)" stroke="none"/>
      </svg>
      0472519306
    </p>
  </div>

  <div class="details">
    <p class="contact-line address">
      <svg class="icon" viewBox="0 0 24 24">
        <path d="M12 2a7 7 0 0 0-7 7c0 5 7 13 7 13s7-8 7-13a7 7 0 0 0-7-7z" fill="var(--blue-bright)"/>
        <circle cx="12" cy="9" r="2.6" fill="var(--card)"/>
      </svg>
      <span>14 Karrabee Drive<br>Kelbrook 3557</span>
    </p>
    <p class="contact-line">
      <svg class="icon" viewBox="0 0 24 24" fill="none" stroke="var(--blue-bright)" stroke-width="2">
        <rect x="3" y="6" width="18" height="13" rx="1"/>
        <path d="M3 7l9 6 9-6"/>
      </svg>
      crestlineplumbing@mailbay.com.au
    </p>
    <p class="contact-line">ABN 64 915 207 338</p>
  </div>
</section>

<section class="card card--back" aria-label="Business card back">
  <div class="brand">
    <span class="brand-dot"></span>
    <span>Crestline<br>Plumbing<br>and Gas</span>
  </div>

  <div class="services">
    <p class="service">
      <svg class="tick" viewBox="0 0 24 24" fill="none" stroke="var(--blue-bright)" stroke-width="2.5"><path d="M3 13l6 6L21 5"/></svg>
      Domestic
    </p>
    <p class="service">
      <svg class="tick" viewBox="0 0 24 24" fill="none" stroke="var(--blue-bright)" stroke-width="2.5"><path d="M3 13l6 6L21 5"/></svg>
      Commercial
    </p>
    <p class="service">
      <svg class="tick" viewBox="0 0 24 24" fill="none" stroke="var(--blue-bright)" stroke-width="2.5"><path d="M3 13l6 6L21 5"/></svg>
      Maintenance
    </p>
  </div>
</section>

</body>
</html>
```